Health Care Company with Logo Needs Business Cards designed

We are a luxury behavioral health company looking for business cards design we already have a logo and are looking for someone to design a sophisticated luxurious looking business card. Please note that Card design should be captivating just like the logo and also encompass the logo color

Industry/Entity Type

Healthcare

Contact Information for Business Card

Logo,company name, tagline, my name and title, contact details, and physical address

```html
<!DOCTYPE html>
<html lang="en">
<head>
<meta charset="utf-8">
<title>Corvane Behavioral Health – Business Card</title>
<link href="https://fonts.googleapis.com/css2?family=Roboto+Condensed:wght@400;700&display=swap" rel="stylesheet">
<style>
  :root {
    --stage: #2a2a2c;
    --card: #1a1a1b;
    --purple: #8a3fa6;
    --blue: #00aeef;
    --orange: #f7931e;
    --green: #7cc242;
    --text: #f2f2f2;
  }
  html, body {
    margin: 0;
    width: 1200px;
    height: 900px;
    overflow: hidden;
    background: var(--stage);
    font-family: "Roboto Condensed", Arial, sans-serif;
  }
  .card {
    position: absolute;
    left: 120px;
    top: 176px;
    width: 960px;
    height: 548px;
    background: var(--card);
    box-shadow: 0 20px 50px rgba(0,0,0,.55);
    color: var(--text);
    overflow: hidden;
  }
  .colour-bands {
    position: absolute;
    left: 0;
    top: 0;
    width: 960px;
    height: 548px;
  }
  .brand {
    position: absolute;
    left: 64px;
    top: 58px;
    display: flex;
    align-items: center;
    gap: 16px;
  }
  .brand-dot {
    width: 22px;
    height: 22px;
    border-radius: 50%;
    background: var(--purple);
  }
  .brand-name {
    font-size: 40px;
    font-weight: 700;
    color: var(--purple);
    letter-spacing: .5px;
  }
  .tagline {
    position: absolute;
    left: 102px;
    top: 112px;
    font-size: 13px;
    font-weight: 700;
    letter-spacing: 2.6px;
    color: var(--blue);
    text-transform: uppercase;
  }
  .person {
    position: absolute;
    left: 64px;
    top: 176px;
  }
  .person-name {
    font-size: 30px;
    font-weight: 700;
    color: var(--blue);
    text-transform: uppercase;
    margin: 0;
  }
  .person-title {
    font-size: 20px;
    margin: 4px 0 0;
  }
  .address {
    position: absolute;
    left: 64px;
    top: 262px;
    font-size: 20px;
    line-height: 1.35;
    font-style: normal;
  }
  .contacts {
    position: absolute;
    left: 64px;
    top: 348px;
    list-style: none;
    margin: 0;
    padding: 0;
    font-size: 20px;
    line-height: 1.45;
  }
  .contacts li {
    display: flex;
    align-items: center;
    gap: 10px;
  }
  .contacts svg { width: 16px; height: 16px; flex: none; }
</style>
</head>
<body>
  <main class="card">
    <svg class="colour-bands" viewBox="0 0 960 548" aria-hidden="true">
      <polygon points="440,548 700,548 860,392 600,392" fill="var(--blue)"/>
      <polygon points="640,370 840,370 960,254 960,186 832,186" fill="var(--orange)"/>
    </svg>

    <div class="brand">
      <span class="brand-dot"></span>
      <span class="brand-name">Corvane Behavioral Health</span>
    </div>
    <div class="tagline">Dedicated to hope, healing and recovery</div>

    <div class="person">
      <h1 class="person-name">Dana Whitlock</h1>
      <p class="person-title">President</p>
    </div>

    <address class="address">
      18320 Marlow Cove Drive<br>
      Seabrook CA 90417
    </address>

    <ul class="contacts">
      <li>
        <svg viewBox="0 0 16 16" aria-hidden="true"><path fill="var(--orange)" d="M4 1l2.5 3-1.5 1.5c.8 2 2.5 3.7 4.5 4.5L11 8.5l3 2.5-1.5 3C7 13.5 2.5 9 2 3z"/></svg>
        555-318-4720
      </li>
      <li>
        <svg viewBox="0 0 16 16" aria-hidden="true"><rect x="1" y="3" width="14" height="10" fill="var(--green)"/><path d="M1 3l7 6 7-6" fill="none" stroke="var(--card)" stroke-width="1.5"/></svg>
        info@corvanehealth.com
      </li>
      <li>
        <svg viewBox="0 0 16 16" aria-hidden="true"><circle cx="8" cy="8" r="6.5" fill="none" stroke="var(--purple)" stroke-width="1.8"/><path d="M1.5 8h13M8 1.5c-3 3.5-3 9.5 0 13M8 1.5c3 3.5 3 9.5 0 13" fill="none" stroke="var(--purple)" stroke-width="1.2"/></svg>
        www.corvanehealth.com
      </li>
    </ul>
  </main>
</body>
</html>
```